New Innovative Counselling and psychotherapy Service needs Business Card design

Keep it simple and professional. On one side, just company name and logo (perhaps in all blue) and maybe a tag line.

On other side (all white) my name and Qualifications in centre

Industry/Entity Type

Health And Wellness

Contact Information for Business Card

Derek Hollis
Counsellor & Psychotherapist
BSc (Psychol.), BA, Dip. (Couns. & Psych.), PG.Cert (CBT), ADLnR, ESGW

I will also require Mobile no, Email and web site address of which I'll pass on to final designer.

Font styles to use
Sans Serif

Requirements
Must have
• My Logo Only and please use the colours in logo that is in it.
Should not have
• Any other images

```html
<!DOCTYPE html>
<html lang="en">
<head>
<meta charset="utf-8">
<title>BrightLane Business Card</title>
<link href="https://fonts.googleapis.com/css2?family=Open+Sans:wght@300;400;600&display=swap" rel="stylesheet">
<style>
  :root {
    --page-bg: #2b2b2b;
    --card-bg: #1d1d1e;
    --card-edge: #262627;
    --brand-blue: #3aaee2;
    --brand-green: #8dc640;
    --text-white: #f2f2f2;
    --text-soft: #e4e4e4;
    --deco-light: #e8e8e8;
    --deco-dark: #3a3a3a;
  }
  * { margin: 0; padding: 0; box-sizing: border-box; }
  html, body {
    width: 1200px; height: 900px; overflow: hidden;
    background: var(--page-bg);
    font-family: "Open Sans", Arial, sans-serif;
  }
  .canvas {
    position: relative; width: 1200px; height: 900px;
  }
  .card {
    position: absolute; left: 250px; width: 700px; height: 400px;
    background: linear-gradient(135deg, var(--card-bg) 0%, var(--card-edge) 100%);
    overflow: hidden;
    box-shadow: 0 12px 30px rgba(0,0,0,0.45);
  }
  .card--front { top: 35px; }
  .card--back { top: 465px; }

  .decoration {
    position: absolute; width: 340px; height: 340px; border-radius: 50%;
    background: radial-gradient(circle at 70% 35%, var(--deco-light) 0%, #9a9a9a 35%, var(--deco-dark) 75%);
  }
  .card--front .decoration { left: -150px; top: -140px; }
  .card--back .decoration { right: -170px; top: 30px;
    background: radial-gradient(circle at 30% 40%, var(--deco-light) 0%, #9a9a9a 35%, var(--deco-dark) 75%); }

  .brand {
    position: absolute; display: flex; align-items: center; gap: 16px;
  }
  .brand__dot {
    width: 44px; height: 44px; border-radius: 50%; background: var(--brand-blue);
  }
  .brand__name {
    font-weight: 300; color: var(--text-white); font-size: 34px; letter-spacing: 1px;
  }
  .card--front .brand { left: 330px; top: 160px; }
  .card--back .brand { left: 45px; top: 40px; }
  .card--back .brand__name { font-size: 30px; }
  .card--back .brand__dot { width: 40px; height: 40px; }

  .web {
    font-size: 16px; color: var(--text-white); letter-spacing: 0.5px;
  }
  .web__domain { color: var(--brand-green); }
  .card--front .web { position: absolute; right: 50px; bottom: 30px; }

  .person { position: absolute; left: 60px; top: 120px; }
  .person__name {
    font-weight: 600; color: var(--brand-blue); font-size: 32px; letter-spacing: 0.5px; line-height: 1.1;
  }
  .person__role, .person__quals {
    color: var(--text-soft); font-size: 17px; line-height: 1.4; letter-spacing: 0.5px;
  }
  .contacts { position: absolute; left: 60px; top: 290px; list-style: none; }
  .contacts li {
    display: flex; align-items: center; gap: 12px;
    color: var(--text-white); font-size: 18px; line-height: 1.45; letter-spacing: 0.5px;
  }
  .contacts svg { width: 14px; height: 14px; flex: none; }
</style>
</head>
<body>
<main class="canvas">
  <section class="card card--front" aria-label="Card front">
    <div class="decoration" role="img" aria-label="Large soft grey emblem decoration"></div>
    <div class="brand">
      <span class="brand__dot"></span>
      <span class="brand__name">BrightLane</span>
    </div>
    <p class="web">www.<span class="web__domain">brightlane</span>.com</p>
  </section>

  <section class="card card--back" aria-label="Card back">
    <div class="decoration" role="img" aria-label="Large soft grey emblem decoration"></div>
    <div class="brand">
      <span class="brand__dot"></span>
      <span class="brand__name">BrightLane</span>
    </div>
    <div class="person">
      <h1 class="person__name">DEREK HOLLIS</h1>
      <p class="person__role">Counsellor &amp; Psychotherapist</p>
      <p class="person__quals">BSc (Psychol.), BA, Dip.<br>(Couns. &amp; Psych.), PG.Cert<br>(CBT), ADLnR, ESGW</p>
    </div>
    <ul class="contacts">
      <li>
        <svg viewBox="0 0 16 16" aria-hidden="true"><path d="M4 1l2.5 3-1.5 2c1 2 2.5 3.5 4.5 4.5l2-1.5 3 2.5-1.5 3C7 14 2 9 1 2.5z" fill="var(--brand-blue)"/></svg>
        555-014-2279
      </li>
      <li>
        <svg viewBox="0 0 16 16" aria-hidden="true"><rect x="1.5" y="3.5" width="13" height="9" fill="none" stroke="var(--brand-blue)" stroke-width="1.5"/><path d="M1.5 3.5L8 9l6.5-5.5" fill="none" stroke="var(--brand-blue)" stroke-width="1.5"/></svg>
        info@brightlane.com
      </li>
      <li>
        <svg viewBox="0 0 16 16" aria-hidden="true"><circle cx="8" cy="8" r="6.5" fill="none" stroke="var(--brand-blue)" stroke-width="1.3"/><ellipse cx="8" cy="8" rx="3" ry="6.5" fill="none" stroke="var(--brand-blue)" stroke-width="1.1"/><path d="M1.5 8h13M2.5 5h11M2.5 11h11" stroke="var(--brand-blue)" stroke-width="1"/></svg>
        <span class="web">www.<span class="web__domain">brightlane</span>.com</span>
      </li>
    </ul>
  </section>
</main>
</body>
</html>
```